Dunmore Associates Banner Add

We are an international headhunting firm looking to target IT guys in Europe and USA to come and work in Singapore or Sydney (Australia). These guys will generally work in Trading firms / Banks / Top Tech Firms. Text - "Are you working in the Fin/ Tech space for a bank or High Frequency Trading firm as a technologist?We have your job in Singapore/ Sydney.Better / Great LifestyleWorking visa'sThe highest calibre clients.Bored with Brexit?Apply now.We need 5 pictures to rotate on a banner add to attract attention / represent this call to action.Some ideas… Guy on a laptop on a beach Sydney Skyline Singapore Skyline Bondi Beach Paradise beach picturesPeople playing on Beach London in the rain vs Sydney (sunny)Style needs to be classy, premium, well finished, boutique and in keeping with our website www.dunmore-associates-example.net. - hence any text you think could be worthwhile taking from there is fine.File formats: JPG, PNG, GIF Maximum file size: 3MB Media Sizes: Minimum: 600 × 315 pixels Recommended: 1200 × 628 pixels Image ratio: 1.91:1 To maximize advert delivery, Images need to be public property, no copyright. 5 rotating pictures incorporating the text, pictures and sell to create one banner add.

Target Market(s)

Banking/ Finance

Number of Pages Required

1 page

Requirements
Must have
• 5 different banners on rotate
Nice to have
• Classy, text suggested or snippets of as required, maybe black and white to match our logo's but injections of colour but full colour is also fine I could be converted.
Should not have
• not too flashy, should be elegant, classy pictures, clean like our website.
• www.dunmore-associates-example.net

```html
<!DOCTYPE html>
<html lang="en">
<head>
<meta charset="utf-8">
<title>Dunmore Associates — Rotating Banner Set</title>
<link rel="stylesheet" href="https://fonts.googleapis.com/css2?family=Barlow:wght@300;400;500&display=swap">
<style>
  :root {
    --paper: #ffffff;
    --ink: #111111;
    --ink-soft: #2a2a2a;
    --grey-dark: #3a3a3a;
    --grey-mid: #8a8a8a;
    --grey-light: #cfcfcf;
    --button: #0d0d0d;
  }
  * { box-sizing: border-box; margin: 0; padding: 0; }
  html, body { width: 1200px; height: 1200px; overflow: hidden; background: var(--paper); }
  body { position: relative; font-family: "Barlow", Arial, sans-serif; color: var(--ink); }

  .brand-header {
    position: absolute; left: 438px; top: 76px; width: 324px; text-align: center;
  }
  .brand-header .brand-name {
    font-weight: 400; font-size: 34px; line-height: 42px; letter-spacing: 10px;
    text-transform: uppercase; color: var(--ink);
  }
  .brand-header .brand-tagline {
    margin-top: 8px; font-weight: 300; font-size: 15px; letter-spacing: 4px;
    text-transform: uppercase; color: var(--grey-dark);
  }

  .banner-number {
    position: absolute; font-family: Arial, sans-serif; font-weight: 700; font-size: 15px; color: var(--ink);
  }

  .banner { position: absolute; background: var(--paper); }
  .banner .photo-strip, .banner .photo { position: absolute; top: 0; height: 100%; }
  .banner .panel {
    position: absolute; top: 0; height: 100%;
    display: flex; flex-direction: column; align-items: center; text-align: center;
  }
  .mini-brand { margin-top: 26px; text-align: center; }
  .mini-brand .name {
    font-weight: 400; font-size: 10px; line-height: 13px; letter-spacing: 2.6px;
    text-transform: uppercase; color: var(--ink);
  }
  .mini-brand .tag {
    font-weight: 300; font-size: 4.6px; letter-spacing: 1px; text-transform: uppercase; color: var(--grey-mid);
  }
  .headline { font-weight: 300; color: var(--ink-soft); }
  .headline b { font-weight: 500; color: var(--ink); }
  .apply-button {
    display: inline-block; width: 86px; height: 22px; line-height: 22px; border-radius: 3px;
    background: var(--button); color: var(--paper); font-size: 9px; font-weight: 500; text-align: center;
  }
  .framed { border: 1px solid var(--ink); }
</style>
</head>
<body>

<header class="brand-header">
  <div class="brand-name">Dunmore<br>Associates</div>
  <div class="brand-tagline">Boutique Executive Search</div>
</header>

<!-- Banner 1 -->
<span class="banner-number" style="left:45px;top:256px">1</span>
<section class="banner" style="left:64px;top:256px;width:515px;height:270px">
  <div class="photo-strip" role="img" aria-label="Edge of harbour photograph" style="left:0;width:26px;background:linear-gradient(180deg,#bdbdbd,#8a8a8a 40%,#3c3c3c)"></div>
  <div class="panel" style="left:26px;width:173px">
    <div class="mini-brand"><div class="name">Dunmore<br>Associates</div><div class="tag">Boutique Executive Search</div></div>
    <p class="headline" style="margin-top:30px;font-size:18px;line-height:29px">We have your<br><b>job available<br>in Singapore<br>and Sydney</b></p>
    <span class="apply-button" style="margin-top:28px">Apply now</span>
  </div>
  <div class="photo" role="img" aria-label="Black and white photograph of Sydney Opera House on the harbour" style="left:199px;width:316px;background:linear-gradient(180deg,#c9c9c9 0%,#a5a5a5 30%,#d8d8d8 55%,#5a5a5a 80%,#2a2a2a 100%)"></div>
</section>

<!-- Banner 2 -->
<span class="banner-number" style="left:597px;top:256px">2</span>
<section class="banner" style="left:616px;top:253px;width:527px;height:273px">
  <div class="photo-strip" role="img" aria-label="Edge of night skyline photograph" style="left:0;width:26px;background:linear-gradient(180deg,#9a9a9a,#444 50%,#222)"></div>
  <div class="panel" style="left:26px;width:176px">
    <div class="mini-brand"><div class="name">Dunmore<br>Associates</div><div class="tag">Boutique Executive Search</div></div>
    <p class="headline" style="margin-top:16px;font-size:14px;line-height:25px">Since our inception,<br><b>Dunmore Associates</b><br>has been solely<br><b>focused on building<br>a strategic, quality,<br>search practice.</b></p>
    <span class="apply-button" style="margin-top:14px">Apply now</span>
  </div>
  <div class="photo" role="img" aria-label="Black and white photograph of a city skyline at night over the harbour" style="left:202px;width:325px;background:linear-gradient(180deg,#a8a8a8 0%,#6a6a6a 35%,#3a3a3a 70%,#1e1e1e 100%)"></div>
</section>

<!-- Banner 3 -->
<span class="banner-number" style="left:45px;top:558px">3</span>
<section class="banner" style="left:64px;top:560px;width:514px;height:270px">
  <div class="photo-strip" role="img" aria-label="Edge of workspace photograph" style="left:0;width:24px;background:linear-gradient(90deg,#d8d8d8,#9c9c9c)"></div>
  <div class="panel" style="left:24px;width:173px">
    <div class="mini-brand"><div class="name">Dunmore<br>Associates</div><div class="tag">Boutique Executive Search</div></div>
    <p class="headline" style="margin-top:16px;font-size:15px;line-height:24.5px">Are you working<br>in the <b>Fin/Tech</b><br>space for a bank<br>or <b>High Frequency<br>Trading firm</b> as<br>a technologist?</p>
    <span class="apply-button" style="margin-top:8px">Apply now</span>
  </div>
  <div class="photo" role="img" aria-label="Black and white photograph of hands typing on a laptop at a desk" style="left:197px;width:317px;background:linear-gradient(160deg,#e6e6e6 0%,#bdbdbd 40%,#8e8e8e 65%,#cfcfcf 100%)"></div>
</section>

<!-- Banner 4 -->
<span class="banner-number" style="left:597px;top:558px">4</span>
<section class="banner" style="left:618px;top:555px;width:521px;height:271px">
  <div class="photo-strip" role="img" aria-label="Edge of coastline photograph" style="left:0;width:27px;background:linear-gradient(180deg,#6a6a6a,#2e2e2e 60%,#4a4a4a)"></div>
  <div class="panel" style="left:27px;width:173px">
    <div class="mini-brand"><div class="name">Dunmore<br>Associates</div><div class="tag">Boutique Executive Search</div></div>
    <p class="headline" style="margin-top:24px;font-size:16.5px;line-height:25.6px">Benefit from<br>fantastic <b>lifestyle<br>working visas</b><br>and the <b>highest<br>calibre clients</b></p>
    <span class="apply-button" style="margin-top:24px">Apply now</span>
  </div>
  <div class="photo" role="img" aria-label="Black and white photograph of an ocean rock pool with swimmers beside the sea" style="left:200px;width:321px;background:linear-gradient(170deg,#5a5a5a 0%,#8a8a8a 25%,#cfcfcf 55%,#a3a3a3 80%,#3a3a3a 100%)"></div>
</section>

<!-- Banner 5 -->
<span class="banner-number" style="left:45px;top:864px">5</span>
<section class="banner framed" style="left:66px;top:866px;width:520px;height:273px">
  <div class="photo-strip" role="img" aria-label="Edge of London cityscape photograph" style="left:0;width:26px;background:linear-gradient(180deg,#bcbcbc,#777 50%,#555)"></div>
  <div class="panel" style="left:26px;width:173px">
    <div class="mini-brand"><div class="name">Dunmore<br>Associates</div><div class="tag">Boutique Executive Search</div></div>
    <p class="headline" style="margin-top:38px;font-size:22px;line-height:32px">Are you<br><b>bored with<br>Brexit?</b></p>
    <span class="apply-button" style="margin-top:42px">Apply now</span>
  </div>
  <div class="photo" role="img" aria-label="Black and white aerial photograph of London with the Elizabeth Tower and Westminster" style="left:199px;width:320px;background:linear-gradient(180deg,#cfcfcf 0%,#9a9a9a 30%,#6e6e6e 60%,#8c8c8c 100%)"></div>
</section>

</body>
</html>
```